Business Card Design Project

Basic business card with minimal details. I just need company name, email & web address, telephone and my name.
I would like the back of the card to be grey with my logo & company name centred.

Target Market(s)

Architects
Builders
Property Developers

Industry/Entity Type

Business

Font styles to use
Sans Serif

Colors

Designer to choose colors to be used in the design.

Requirements
Must have
• Venture Frame
Marcus Hadley - Director
M: 0452 913084
E: marcus@ventureframe.com.au
W: www.ventureframe.com.au
Should not have
• No other images or pictures

```html
<!DOCTYPE html>
<html lang="en">
<head>
<meta charset="utf-8">
<title>Venture Frame – Business Card</title>
<link rel="stylesheet" href="https://fonts.googleapis.com/css2?family=Raleway:wght@400;500;600&family=Nunito+Sans:wght@400&display=swap">
<style>
  :root {
    --canvas: #f1f1f2;
    --card-white: #ffffff;
    --card-grey: #d8d9e1;
    --brand-red: #a8122f;
    --band-red: #b31f2b;
    --band-dark: #2a0306;
    --slate: #4a5663;
    --ink: #1d1d1f;
  }
  * { box-sizing: border-box; margin: 0; padding: 0; }
  html, body {
    width: 1200px;
    height: 1200px;
    overflow: hidden;
    background: var(--canvas);
  }
  .sheet {
    position: relative;
    width: 1200px;
    height: 1200px;
  }
  .card {
    position: absolute;
    left: 174px;
    width: 853px;
    height: 488px;
    overflow: hidden;
  }
  .card--front { top: 69px; background: var(--card-white); }
  .card--back { top: 643px; background: var(--card-grey); }

  .brand {
    display: flex;
    align-items: center;
    gap: 16px;
    font-family: "Raleway", sans-serif;
    font-weight: 600;
    color: var(--slate);
    letter-spacing: 0.04em;
    text-transform: uppercase;
    white-space: nowrap;
  }
  .brand__dot {
    flex: none;
    border-radius: 50%;
    background: var(--brand-red);
  }
  .card--front .brand {
    position: absolute;
    left: 64px;
    top: 58px;
    font-size: 38px;
  }
  .card--front .brand__dot { width: 52px; height: 52px; }

  .band {
    position: absolute;
    left: 0;
    top: 168px;
    width: 100%;
    height: 33px;
    background: linear-gradient(to bottom, var(--band-dark) 0%, var(--band-red) 55%, var(--band-red) 100%);
  }

  .person {
    position: absolute;
    left: 400px;
    top: 236px;
  }
  .person__name {
    font-family: "Raleway", sans-serif;
    font-weight: 500;
    font-size: 40px;
    line-height: 1.1;
    color: var(--brand-red);
  }
  .person__title {
    font-family: "Raleway", sans-serif;
    font-weight: 400;
    font-size: 27px;
    line-height: 1.2;
    color: var(--ink);
  }
  .contact {
    position: absolute;
    left: 404px;
    top: 352px;
    font-family: "Nunito Sans", sans-serif;
    font-weight: 400;
    font-size: 25px;
    color: var(--ink);
    border-collapse: collapse;
  }
  .contact th {
    font-weight: 400;
    text-align: left;
    width: 46px;
    padding: 0;
    line-height: 33px;
  }
  .contact td { padding: 0; line-height: 33px; letter-spacing: 0.01em; }

  .card--back .brand {
    position: absolute;
    left: 50%;
    top: 50%;
    transform: translate(-50%, -10%);
    font-size: 36px;
  }
  .card--back .brand__dot { width: 48px; height: 48px; }
</style>
</head>
<body>
<main class="sheet">
  <section class="card card--front" aria-label="Business card front">
    <div class="brand">
      <span class="brand__dot" aria-hidden="true"></span>
      <span class="brand__name">Venture Frame</span>
    </div>
    <div class="band" aria-hidden="true"></div>
    <div class="person">
      <h1 class="person__name">Marcus Hadley</h1>
      <p class="person__title">Director</p>
    </div>
    <table class="contact">
      <tr><th>M:</th><td>0452 913084</td></tr>
      <tr><th>E:</th><td>marcus@ventureframe.com.au</td></tr>
      <tr><th>W</th><td>www.ventureframe.com.au</td></tr>
    </table>
  </section>

  <section class="card card--back" aria-label="Business card back">
    <div class="brand">
      <span class="brand__dot" aria-hidden="true"></span>
      <span class="brand__name">Venture Frame</span>
    </div>
  </section>
</main>
</body>
</html>
```